Purchasing community for life science startups needs landing page for collecting of contact adresses

We are the "Vessel Alliance", the first purchasing community for life science startups. The idea is to bundle the needs of several smaller companies (laboratories) and to buy lab consumables and chemicals in larger quantities. This bargaining position, at the end of all participants can buy their products very low prices. In the attached powerpoint file you will find an idea and some elements, which demonstrate a little the style, which came into my mind.
Target Market(s)
Our target customers are startups and smaller biotech companies, which are too small to get the best prices. The aim of this landing page is to collect all interested parties.
Look and feel
Each slider illustrates characteristics of the customer's brand and the style your logo design should communicate.

```html
<!DOCTYPE html>
<html lang="en">
<head>
<meta charset="utf-8">
<title>Vessel Alliance – Joint Purchase at Wholesale Prices</title>
<link href="https://fonts.googleapis.com/css2?family=Roboto:wght@400;500;700&family=Raleway:wght@400;500&display=swap" rel="stylesheet">
<style>
:root{
  --blue:#1e8fd6;
  --blue-bright:#1a9be6;
  --sky:#5cc6ec;
  --navy:#0d3a6e;
  --deep:#1a4f86;
  --ink:#222;
  --muted:#3a3a3a;
  --panel:#efefef;
  --footer:#0e0e0e;
  --white:#fff;
}
*{box-sizing:border-box;margin:0;padding:0}
html,body{width:761px;height:1200px;overflow:hidden}
body{position:relative;background:var(--white);font-family:Roboto,Arial,sans-serif;color:var(--ink)}
.abs{position:absolute}

/* header */
.hero-bg{left:0;top:0;width:761px;height:470px;background:radial-gradient(ellipse at 60% 40%,#fff 0%,#f1f1f1 60%,#e6e6e6 100%)}
.brand{left:100px;top:22px;display:flex;align-items:center;gap:7px}
.brand-mark{width:41px;height:41px;background:var(--deep)}
.brand-name{font-weight:700;font-size:16px;letter-spacing:.2px;line-height:1;color:#111}
.brand-tag{font-size:8.5px;color:#222;margin-top:2px}
.nav{left:342px;top:27px;display:flex;gap:24px;font-size:11.5px;font-weight:500;color:#2a2a2a}
.nav .active{color:var(--blue)}

.hero-title{left:100px;top:130px;font-size:24px;font-weight:700;line-height:27px;color:var(--blue)}
.hero-copy{left:103px;top:196px;width:255px;font-size:12.4px;line-height:17.2px;color:var(--navy)}
.hero-copy p+p{margin-top:17px}
.hero-art{left:362px;top:135px;width:326px;height:210px;background:linear-gradient(90deg,#d7ecd9 0%,#f3e39a 25%,#f2b2b2 50%,#b6e3a6 72%,#cdb6ea 100%);border-radius:10px;opacity:.85}

.wave{left:0;width:761px}

/* benefits */
.frame{left:103px;top:511px;width:242px;height:185px;background:var(--blue-bright);clip-path:polygon(0 0,100% 0,90% 10%,10% 10%,10% 100%,0 88%)}
.photo{left:117px;top:525px;width:241px;height:185px;background:linear-gradient(135deg,#eef0f4,#c9ced8 60%,#9aa3b3)}
.benefits{left:384px;top:532px;width:275px}
.benefits h2{font-family:Raleway,sans-serif;font-weight:400;font-size:22px;color:#111}
.benefits .rule{width:65px;height:2px;background:var(--blue);margin:7px 0 10px 2px}
.ticks{list-style:none;font-size:8px;line-height:15.6px;color:var(--muted);margin-left:2px}
.ticks li{display:flex;align-items:center;gap:4px}
.ticks i{display:inline-block;width:8px;height:8px;border-radius:50%;background:var(--blue)}
.benefits p{font-size:7.8px;line-height:15.6px;color:var(--muted);margin-left:2px;text-align:justify}
.benefits p.gap{margin-top:6px}

/* lower */
.panel-left{left:0;top:750px;width:382px;height:330px;background:var(--panel)}
.panel-right{left:382px;top:750px;width:379px;height:330px;background:radial-gradient(circle at 60% 50%,#2d7db5,#1b5b93 70%,#174e80)}
.feature{left:98px;width:245px;display:flex;gap:12px}
.feature svg{flex:none;margin-top:2px}
.feature h3{font-family:Raleway,sans-serif;font-weight:500;font-size:14px;color:#111;margin-bottom:3px}
.feature p{font-size:7.6px;line-height:11.8px;color:#222;text-align:justify}

.form{left:416px;top:842px;width:239px}
.field{height:37px;background:var(--white);border:1px solid #cfd8e2;margin-bottom:7.5px;font-size:9.5px;padding:0 11px;display:flex;align-items:center;color:#222}
.submit{height:37px;background:var(--blue-bright);color:var(--white);font-size:12px;display:flex;align-items:center;justify-content:center}

.footer{left:0;top:1110px;width:761px;height:90px;background:var(--footer)}
.foot-text{left:106px;top:1135px;font-size:10px;line-height:22px;color:var(--white)}
.social{left:583px;top:1156px;display:flex;gap:8px}
.social span{width:14px;height:14px;background:var(--white);border-radius:2px}
</style>
</head>
<body>

<div class="abs hero-bg"></div>

<div class="abs brand">
  <div class="brand-mark"></div>
  <div>
    <div class="brand-name">VESSEL ALLIANCE</div>
    <div class="brand-tag">Lab Purchasing Network</div>
  </div>
</div>

<nav class="abs nav">
  <span class="active">HOME</span><span>ABOUT US</span><span>SERVICES</span><span>WHY US</span><span>CONTACT</span>
</nav>

<h1 class="abs hero-title">JOINT PURCHASE AT<br>WHOLESALE PRICES</h1>
<div class="abs hero-copy">
  <p>Do you run a LifeScience lab?<br>Do you need chemicals, laboratory glassware and consumables regularly?<br>Are your purchase quantities too small to receive maximum discounts?</p>
  <p>Then take part in the first lab campaign 2019 and Save up to 40% on purchases.</p>
</div>
<div class="abs hero-art" role="img" aria-label="Row of laboratory flasks and cylinders filled with green, yellow, red and purple liquids"></div>

<svg class="abs wave" style="top:380px" width="761" height="95" viewBox="0 0 761 95">
  <path d="M0 95 L0 60 C150 90 300 35 480 25 C600 18 700 28 761 38 L761 95 Z" fill="#fff"/>
  <path d="M0 15 C160 40 330 15 500 8 C640 2 720 20 761 40 L761 55 C700 40 600 30 470 36 C300 45 150 70 0 52 Z" fill="var(--sky)"/>
  <path d="M0 50 C160 72 320 45 480 32 C620 22 710 34 761 52 L761 58 C700 44 600 40 480 48 C320 60 160 90 0 82 Z" fill="var(--deep)"/>
</svg>

<div class="abs frame"></div>
<div class="abs photo" role="img" aria-label="Person touching a network of digital currency nodes"></div>

<section class="abs benefits">
  <h2>Benefits for participants</h2>
  <div class="rule"></div>
  <ul class="ticks">
    <li><i></i>Buy at wholesale prices</li>
    <li><i></i>No negotiations with suppliers</li>
    <li><i></i>No contract obligation</li>
  </ul>
  <p>Are you interested in participating?<br>Then please do not hesitate to sign up for our list of interested parties.</p>
  <p class="gap">To get an impression of our prices, we send you a preliminary price list and ask for feedback. Which articles interest you? In what quantities do you need these? Which are still missing?</p>
</section>

<div class="abs panel-left"></div>
<div class="abs panel-right" role="img" aria-label="Blue background with glowing digital coin pattern"></div>

<svg class="abs wave" style="top:735px" width="761" height="60" viewBox="0 0 761 60">
  <path d="M0 0 H761 V12 C710 10 620 18 480 14 C320 8 160 8 0 30 Z" fill="#fff"/>
  <path d="M0 30 C160 8 320 8 480 14 C620 18 710 10 761 12 L761 30 C700 22 600 26 470 26 C320 26 160 30 0 45 Z" fill="var(--sky)"/>
</svg>

<div class="abs feature" style="top:804px">
  <svg width="24" height="26" viewBox="0 0 24 26"><path d="M9 1h6v2h-1v7l8 13a2 2 0 0 1-2 3H4a2 2 0 0 1-2-3l8-13V3H9z" fill="var(--blue)"/></svg>
  <div><h3>Our Goal</h3><p>is to build the first LifeScience Laboratory purchasing community, which allows each participant to cover their laboratory supplies at wholesale prices.</p></div>
</div>
<div class="abs feature" style="top:877px">
  <svg width="24" height="28" viewBox="0 0 24 28"><path d="M1 2h22v12c0 7-6 11-11 13C6 25 1 21 1 14z" fill="var(--blue)"/><path d="M7 6h4v14C8 18 7 16 7 13z" fill="#fff"/></svg>
  <div><h3>The campaign principle</h3><p>We bundle your annual demand for chemicals, consumables and laboratory supplies and act as a strong negotiating partner for manufacturers and suppliers. The more participants participate, the bigger our bargaining power, the better our purchase prices</p></div>
</div>
<div class="abs feature" style="top:973px">
  <svg width="24" height="34" viewBox="0 0 24 34"><rect x="9" y="1" width="5" height="12" rx="1" fill="var(--blue)" transform="rotate(20 11 7)"/><path d="M4 24a8 8 0 0 1 14-6" stroke="var(--blue)" stroke-width="3" fill="none"/><rect x="2" y="28" width="20" height="4" fill="var(--blue)"/></svg>
  <div><h3>Keep it simple</h3><p>We waive framework contracts, minimum order quantities and other obligations! If you like the negotiated price, then you normally order by order in the laboratory campaign your needs.</p></div>
</div>

<form class="abs form">
  <div class="field">Email Address</div>
  <div class="field">Last Name</div>
  <div class="field">First Name</div>
  <div class="submit">Price list received by email</div>
</form>

<div class="abs footer"></div>
<svg class="abs wave" style="top:1060px" width="761" height="60" viewBox="0 0 761 60">
  <path d="M0 0 L761 0 L761 30 C600 20 400 40 200 45 C120 47 50 45 0 42 Z" fill="var(--sky)"/>
  <path d="M0 42 C200 48 400 35 560 28 C660 24 720 28 761 30 L761 60 L0 60 Z" fill="var(--footer)"/>
  <path d="M0 38 C200 44 400 30 560 22 C660 18 720 22 761 26 L761 30 C700 26 600 26 470 34 C300 44 150 50 0 46 Z" fill="var(--deep)"/>
</svg>

<div class="abs foot-text">Vessel Alliance Purchasing e.K<br>Imprint | Data Protection</div>
<div class="abs social" aria-label="Social links"><span></span><span></span><span></span><span></span></div>

</body>
</html>
```